Verbesserung PowerPoint Präsentation PitchDeck
Zielgruppe
Es geht um die Verbesserung eines Startup-PitchDecks (Powerpoint-Präsentation) für eine Consumer-App.
Aufgabenstellung
Es existiert eine vollständige 13seitige PowerPoint Präsentation. Es müssen keine neuen Inhalte kreativ erstellt werden. Es geht ausschließlich nur darum eine bestehende Präsentation zu verbessern, damit das alles etwas runder und professioneller aussieht.
Derjenige der den Auftrag annimmt ist verpflichtet die 13 seitige Präsentation zu verbessern.
Überarbeitung des Briefings am 17.1. 11 Uhr):
Es geht wirklich nur darum, dass eine bestehende Präsentation verbessert wird, so dass diese einfach etwas besser und professioneller aussieht. Um mehr nicht! Deswegen denke ich, dass der ausgeschriebene Preis angemessen ist.
Für die Ausschreibung hatte ich 3 Beispiel-Folien zur Verfügung gestellt und es sollten für diese 3 Beispiel-Folien neue entworfen werden. Die Idee war, dass der Vorschlag der uns am meisten überzeugt den Zuschlag erhält. Irgendwie kommen aber keine Vorschläge. Mir ist bewusst, dass ein "Design-Pitch" für diesen Auftrag sicherlich zu viel des Guten ist und deswegen nehmen wir davon Abstand. Deswegen einfach kurz vorstellen mit ein paar Beispielen/Referenzen und wir entscheiden uns dann.

```html
<!DOCTYPE html>
<html lang="de">
<head>
<meta charset="utf-8">
<title>Pitch Deck – Folienentwurf</title>
<link rel="stylesheet" href="https://fonts.googleapis.com/css2?family=Arimo:wght@400;700&display=swap">
<style>
  :root {
    --orange: #fb8c2f;
    --grey: #808080;
    --grey-line: #9a9a9a;
    --ink: #111111;
    --slide-top: #e6e5e6;
    --slide-bottom: #f2f2f2;
    --paper: #ffffff;
  }
  html, body {
    margin: 0;
    padding: 0;
    width: 820px;
    height: 1200px;
    overflow: hidden;
    background: var(--paper);
  }
  .deck { display: block; width: 820px; height: 1200px; }
  .deck text { font-family: "Arimo", Arial, Helvetica, sans-serif; }
  .slide-frame { fill: url(#slideShade); }
  .slide-body { fill: var(--paper); }
  .accent-rule { fill: var(--orange); }
  .slide-title { font-size: 38px; font-weight: 700; fill: var(--ink); }
  .slide-meta { font-size: 12px; fill: var(--grey); }
  .bar-label { font-size: 20px; font-weight: 700; fill: var(--paper); }
  .outline-orange { fill: none; stroke: var(--orange); stroke-width: 3; }
  .outline-grey { fill: none; stroke: var(--grey); stroke-width: 3; }
  .fill-orange { fill: var(--orange); }
  .fill-grey { fill: var(--grey); }
  .person-outline { fill: none; stroke: var(--grey); stroke-width: 2; }
  .tether { stroke: #b5b5b5; stroke-width: 1.2; }
  .side-label { font-size: 21px; font-weight: 700; }
  .side-label.orange { fill: var(--orange); }
  .side-label.grey { fill: var(--grey); }
  .box-copy { font-size: 18px; fill: var(--ink); }
  .summary-copy { font-size: 20.5px; fill: var(--ink); }
  .summary-rule { stroke: var(--orange); stroke-width: 3; }
  .hex-edge { stroke: var(--orange); stroke-width: 3; fill: none; }
  .hex-node { fill: var(--orange); }
  .logo-slot { font-size: 29px; fill: var(--ink); }
  .feature-title { font-size: 29px; font-weight: 700; fill: var(--ink); }
  .feature-copy { font-size: 19px; fill: var(--ink); }
  .leader { fill: none; stroke: var(--grey-line); stroke-width: 1.2; }
</style>
</head>
<body>
<svg class="deck" viewBox="0 0 1600 2341" xmlns="http://www.w3.org/2000/svg" xmlns:xlink="http://www.w3.org/1999/xlink">
  <defs>
    <linearGradient id="slideShade" x1="0" y1="0" x2="1" y2="1">
      <stop offset="0" stop-color="var(--slide-top)"/>
      <stop offset="1" stop-color="var(--slide-bottom)"/>
    </linearGradient>
    <symbol id="person" viewBox="0 0 60 80">
      <circle cx="30" cy="17" r="16"/>
      <path d="M2 80 V58 Q2 41 20 39 L30 62 L40 39 Q58 41 58 58 V80 Z"/>
    </symbol>
  </defs>

  <!-- Folie 1 -->
  <g class="slide slide-one">
    <rect class="slide-frame" x="223" y="89" width="1144" height="644"/>
    <text class="slide-title" x="264" y="186">Consetetur</text>
    <rect class="accent-rule" x="264" y="217" width="1061" height="7"/>
    <rect class="slide-body" x="264" y="224" width="1061" height="481"/>

    <g class="company-house">
      <polygon class="fill-orange" points="317,337 470,278 622,337 622,353 470,296 317,353"/>
      <path class="outline-orange" d="M317 572 V374 L470 318 L622 374 V438 H656 V422 L716 468 L656 516 V500 H622 V572"/>
      <use href="#person" class="fill-orange" x="357" y="414" width="63" height="79"/>
      <use href="#person" class="fill-orange" x="443" y="414" width="63" height="79"/>
      <use href="#person" class="person-outline" x="528" y="414" width="64" height="79"/>
      <rect class="fill-orange" x="315" y="572" width="309" height="50"/>
      <text class="bar-label" x="471" y="603" text-anchor="middle">Takima bertus</text>
    </g>

    <g class="audience">
      <g class="tethers">
        <line class="tether" x1="792" y1="433" x2="792" y2="572"/>
        <line class="tether" x1="868" y1="433" x2="868" y2="572"/>
        <line class="tether" x1="943" y1="433" x2="943" y2="572"/>
        <line class="tether" x1="1018" y1="433" x2="1018" y2="572"/>
        <line class="tether" x1="1094" y1="433" x2="1094" y2="572"/>
        <line class="tether" x1="1169" y1="433" x2="1169" y2="572"/>
        <line class="tether" x1="1244" y1="433" x2="1244" y2="572"/>
        <line class="tether" x1="829" y1="492" x2="829" y2="572"/>
        <line class="tether" x1="904" y1="492" x2="904" y2="572"/>
        <line class="tether" x1="979" y1="492" x2="979" y2="572"/>
        <line class="tether" x1="1055" y1="492" x2="1055" y2="572"/>
        <line class="tether" x1="1130" y1="492" x2="1130" y2="572"/>
        <line class="tether" x1="1205" y1="492" x2="1205" y2="572"/>
      </g>
      <g class="fill-grey">
        <use href="#person" x="770" y="379" width="44" height="55"/>
        <use href="#person" x="846" y="379" width="44" height="55"/>
        <use href="#person" x="921" y="379" width="44" height="55"/>
        <use href="#person" x="996" y="379" width="44" height="55"/>
        <use href="#person" x="1072" y="379" width="44" height="55"/>
        <use href="#person" x="1147" y="379" width="44" height="55"/>
        <use href="#person" x="1222" y="379" width="44" height="55"/>
        <use href="#person" x="807" y="437" width="44" height="55"/>
        <use href="#person" x="882" y="437" width="44" height="55"/>
        <use href="#person" x="957" y="437" width="44" height="55"/>
        <use href="#person" x="1033" y="437" width="44" height="55"/>
        <use href="#person" x="1108" y="437" width="44" height="55"/>
        <use href="#person" x="1183" y="437" width="44" height="55"/>
        <use href="#person" x="770" y="496" width="44" height="55"/>
        <use href="#person" x="846" y="496" width="44" height="55"/>
        <use href="#person" x="921" y="496" width="44" height="55"/>
        <use href="#person" x="996" y="496" width="44" height="55"/>
        <use href="#person" x="1072" y="496" width="44" height="55"/>
        <use href="#person" x="1147" y="496" width="44" height="55"/>
        <use href="#person" x="1222" y="496" width="44" height="55"/>
      </g>
      <rect class="fill-grey" x="769" y="572" width="499" height="49"/>
      <text class="bar-label" x="1020" y="603" text-anchor="middle">Taakitama sanctus</text>
    </g>

    <text class="slide-meta" x="273" y="725">1/17/2017</text>
    <text class="slide-meta" x="1317" y="725" text-anchor="end">1</text>
  </g>

  <!-- Folie 2 -->
  <g class="slide slide-two">
    <rect class="slide-frame" x="223" y="833" width="1144" height="644"/>
    <text class="slide-title" x="260" y="930">Nonumy / Eirmod</text>
    <rect class="accent-rule" x="264" y="961" width="1061" height="7"/>
    <rect class="slide-body" x="264" y="968" width="1061" height="481"/>

    <g class="exchange-left">
      <text class="side-label orange" x="286" y="1016">Takima bertus</text>
      <use href="#person" class="fill-orange" x="485" y="983" width="77" height="93"/>
      <path class="outline-orange" d="M469 1037 H286 V1302 H745 V1148 H780 V1164 L840 1117 L780 1070 V1086 H745 V1037 H579"/>
      <g class="box-copy">
        <text x="328" y="1096">At vero eos et accusam et justo duo dolores</text>
        <text x="328" y="1129">Lorem ipsum dolor sit amet, consetetur</text>
        <text x="328" y="1149">sadipscing elitr, sed diam nonumy</text>
        <text x="328" y="1182">Sed diam nonumy eirmod tempor invidunt ut</text>
        <text x="328" y="1202">labore et dolore magna aliquyam erat, sed</text>
        <text x="328" y="1222">diam voluptua.</text>
        <text x="328" y="1255">At vero eos et accusam et justo duo dolores</text>
      </g>
    </g>

    <g class="exchange-right">
      <text class="side-label grey" x="1305" y="1016" text-anchor="end">Taakitama sanctus</text>
      <use href="#person" class="fill-grey" x="1019" y="983" width="77" height="93"/>
      <path class="outline-grey" d="M1002 1037 H846 V1193 H811 V1177 L751 1223 L811 1270 V1254 H846 V1302 H1305 V1037 H1113"/>
      <g class="box-copy">
        <text x="886" y="1096">At vero eos et accusam et justo duo dolores</text>
        <text x="886" y="1129">Lorem ipsum dolor sit amet, consetetur</text>
        <text x="886" y="1149">sadipscing elitr, sed diam nonumy</text>
        <text x="886" y="1182">Sed diam nonumy eirmod tempor invidunt ut</text>
        <text x="886" y="1202">labore et dolore magna aliquyam erat, sed</text>
        <text x="886" y="1222">diam voluptua.</text>
        <text x="886" y="1255">At vero eos et accusam et justo duo dolores</text>
      </g>
    </g>

    <g class="summary">
      <line class="summary-rule" x1="286" y1="1330" x2="1304" y2="1330"/>
      <g class="summary-copy" text-anchor="middle">
        <text x="802" y="1359">Lorem ipsum dolor sit amet, consetetur sadipscing elitr, sed diam nonumy eirmod tempor invidunt ut</text>
        <text x="802" y="1382">labore et dolore magna aliquyam erat, sed diam voluptua. At vero eos et accusam et justo duo dolores</text>
        <text x="802" y="1405">et ea rebum. Stet clita kasd gubergren.</text>
      </g>
      <line class="summary-rule" x1="286" y1="1420" x2="1304" y2="1420"/>
    </g>

    <text class="slide-meta" x="273" y="1469">1/17/2017</text>
    <text class="slide-meta" x="1317" y="1469" text-anchor="end">2</text>
  </g>

  <!-- Folie 3 -->
  <g class="slide slide-three">
    <rect class="slide-frame" x="223" y="1580" width="1144" height="644"/>
    <text class="slide-title" x="260" y="1677">Lorem ipsum dolor sit amet</text>
    <rect class="accent-rule" x="264" y="1708" width="1061" height="7"/>
    <rect class="slide-body" x="264" y="1715" width="1061" height="481"/>

    <g class="hex-ring">
      <polygon class="hex-edge" points="795,1808 916,1871 916,2028 795,2093 672,2028 672,1871"/>
      <circle class="hex-node" cx="795" cy="1808" r="24"/>
      <circle class="hex-node" cx="916" cy="1871" r="24"/>
      <circle class="hex-node" cx="916" cy="2028" r="24"/>
      <circle class="hex-node" cx="795" cy="2093" r="24"/>
      <circle class="hex-node" cx="672" cy="2028" r="24"/>
      <circle class="hex-node" cx="672" cy="1871" r="24"/>
      <text class="logo-slot" x="795" y="1938" text-anchor="middle">IHR</text>
      <text class="logo-slot" x="795" y="1972" text-anchor="middle">LOGO</text>
    </g>

    <g class="leaders">
      <path class="leader" d="M292 1782 H600 L642 1847"/>
      <path class="leader" d="M292 1938 H600 L642 2003"/>
      <path class="leader" d="M292 2094 H754"/>
      <path class="leader" d="M824 1806 H1289"/>
      <path class="leader" d="M936 1897 L978 1962 H1289"/>
      <path class="leader" d="M936 2053 L978 2118 H1289"/>
    </g>

    <g class="features-left">
      <text class="feature-title" x="292" y="1771">Agile Zielgruppe</text>
      <text class="feature-copy" x="292" y="1803">Lorem ipsum dolor sit ametLorem</text>
      <text class="feature-copy" x="292" y="1826">ipsum dolor sit amet</text>
      <text class="feature-title" x="292" y="1927">Einfaches Handling</text>
      <text class="feature-copy" x="292" y="1959">Lorem ipsum dolor sit ametLorem</text>
      <text class="feature-copy" x="292" y="1982">ipsum dolor sit amet</text>
      <text class="feature-title" x="292" y="2083">Bekanntheitsgrad</text>
      <text class="feature-copy" x="292" y="2116">Lorem ipsum dolor sit ametLorem</text>
      <text class="feature-copy" x="292" y="2139">ipsum dolor sit amet</text>
    </g>

    <g class="features-right" text-anchor="end">
      <text class="feature-title" x="1289" y="1799">Marktgröße</text>
      <text class="feature-copy" x="1289" y="1825">Lorem ipsum dolor sit ametLorem</text>
      <text class="feature-copy" x="1289" y="1848">ipsum dolor sit amet</text>
      <text class="feature-title" x="1289" y="1956">Zukunftsweisend</text>
      <text class="feature-copy" x="1289" y="1981">Lorem ipsum dolor sit ametLorem</text>
      <text class="feature-copy" x="1289" y="2004">ipsum dolor sit amet</text>
      <text class="feature-title" x="1289" y="2112">Skalierbarkeit</text>
      <text class="feature-copy" x="1289" y="2138">Lorem ipsum dolor sit ametLorem</text>
      <text class="feature-copy" x="1289" y="2161">ipsum dolor sit amet</text>
    </g>

    <text class="slide-meta" x="273" y="2216">1/17/2017</text>
    <text class="slide-meta" x="1317" y="2216" text-anchor="end">3</text>
  </g>
</svg>
</body>
</html>
```